" Cavalto Solutions oferece serviços de automação de tarefas manuais repetitivas realizadas na administração das empresas, como ingresso de faturas, coleta de dados de vários sistemas e consolidação manual, aceso a site para extração de dados e posterior registro em sistemas próprios, etc. Os serviços que oferece são: a identificação dessas oportunidades apoiando no budiness case, o desenvolvimento dos robôs para automação, a implantação do modelo de governança para assegurar a boa implantação e posterior sustentabilidade, transferência de conhecimento para as equipes internos, e finalmente o suporte e manutenção da plataforma. "

```html
<!DOCTYPE html>
<html lang="pt-BR">
<head>
<meta charset="UTF-8">
<title>Cavalto Solutions — Automação Robótica de Processos</title>
<link rel="stylesheet" href="https://fonts.googleapis.com/css2?family=Oswald:wght@600&family=Open+Sans:wght@400;600;700&display=swap">
<style>
  :root {
    --brand-blue: #1e9fd6;
    --brand-blue-dark: #1580b3;
    --navy: #0b2544;
    --navy-deep: #061a33;
    --hero-glow: #1a5a8c;
    --ink: #2c3e50;
    --muted: #8a96a3;
    --white: #ffffff;
    --page: #ffffff;
  }
  * { box-sizing: border-box; margin: 0; padding: 0; }
  html, body { width: 1200px; height: 1200px; overflow: hidden; background: var(--page); }
  body { font-family: "Open Sans", sans-serif; color: var(--ink); }

  .top-bar {
    height: 40px; background: var(--brand-blue);
    display: flex; align-items: center; justify-content: flex-end;
    padding: 0 70px; gap: 18px; color: var(--white); font-size: 14px;
  }
  .top-bar .phone { display: flex; align-items: center; gap: 8px; }

  .site-header {
    height: 96px; display: flex; align-items: center; justify-content: space-between;
    padding: 0 70px; background: var(--white);
  }
  .brand { display: flex; align-items: center; gap: 14px; }
  .brand-dot { width: 40px; height: 40px; border-radius: 50%; background: var(--brand-blue); }
  .brand-name { font-family: "Open Sans", sans-serif; font-weight: 700; font-size: 26px; color: var(--navy); letter-spacing: .5px; }

  .main-nav { display: flex; align-items: center; gap: 38px; font-size: 16px; font-weight: 600; color: var(--ink); }
  .main-nav .active { color: var(--brand-blue); }
  .main-nav .social { width: 30px; height: 30px; border-radius: 50%; background: var(--brand-blue); }

  .hero { position: relative; height: 690px; overflow: hidden; }
  .hero-art {
    position: absolute; inset: 0;
    background:
      radial-gradient(circle at 72% 40%, #c9d3dc 0, #8c9aa8 12%, transparent 30%),
      radial-gradient(circle at 25% 55%, var(--hero-glow) 0, transparent 45%),
      linear-gradient(110deg, var(--navy-deep) 0%, var(--navy) 45%, #173d63 100%);
  }
  .hero-content { position: absolute; left: 70px; top: 200px; width: 620px; color: var(--white); }
  .hero-title {
    font-family: "Oswald", sans-serif; font-weight: 600; font-size: 70px; line-height: 1.05;
    text-transform: uppercase; letter-spacing: 1px;
  }
  .hero-text { margin-top: 28px; font-size: 17px; line-height: 1.6; max-width: 520px; }
  .btn-primary {
    display: inline-block; margin-top: 30px; padding: 12px 30px; border-radius: 24px;
    background: var(--brand-blue); color: var(--white); font-weight: 600; font-size: 16px;
  }
  .slider-controls {
    position: absolute; right: 90px; bottom: 180px; display: flex; align-items: center; gap: 12px;
  }
  .slider-controls .dot { width: 10px; height: 10px; border-radius: 50%; border: 2px solid var(--white); }
  .slider-controls .dot.current { background: var(--white); }

  .services-intro { text-align: center; padding-top: 58px; }
  .section-title { font-size: 32px; font-weight: 400; color: var(--ink); }
  .section-rule { width: 50px; height: 3px; background: var(--brand-blue); margin: 20px auto; }
  .section-text { font-size: 15px; color: var(--muted); line-height: 1.6; max-width: 560px; margin: 0 auto; }
</style>
</head>
<body>
  <div class="top-bar">
    <span class="phone">
      <svg width="14" height="14" viewBox="0 0 24 24" fill="#fff"><path d="M6.6 10.8a15 15 0 0 0 6.6 6.6l2.2-2.2a1 1 0 0 1 1-.25 11.4 11.4 0 0 0 3.6.57 1 1 0 0 1 1 1V20a1 1 0 0 1-1 1A17 17 0 0 1 3 4a1 1 0 0 1 1-1h3.5a1 1 0 0 1 1 1c0 1.25.2 2.45.57 3.57a1 1 0 0 1-.25 1z"/></svg>
      (11) 4000-1234
    </span>
  </div>

  <header class="site-header">
    <div class="brand">
      <span class="brand-dot"></span>
      <span class="brand-name">Cavalto Solutions</span>
    </div>
    <nav class="main-nav">
      <span class="active">Home</span>
      <span>Quem Somos</span>
      <span>RPA</span>
      <span>Serviços ▾</span>
      <span>Contato</span>
      <span class="social"></span>
    </nav>
  </header>

  <section class="hero">
    <div class="hero-art" role="img" aria-label="Ilustração de um robô humanoide pensativo sobre fundo azul escuro com ícones de tecnologia conectados"></div>
    <div class="hero-content">
      <h1 class="hero-title">Automação Robótica<br>de Processos</h1>
      <p class="hero-text">Automatizamos tarefas manuais e repetitivas da sua empresa, liberando equipes para o que realmente importa no negócio.</p>
      <span class="btn-primary">Saiba mais</span>
    </div>
    <div class="slider-controls">
      <svg width="16" height="20" viewBox="0 0 16 20"><path d="M12 2 4 10l8 8" stroke="#fff" stroke-width="2.5" fill="none"/></svg>
      <span class="dot current"></span><span class="dot"></span><span class="dot"></span>
      <svg width="16" height="20" viewBox="0 0 16 20"><path d="m4 2 8 8-8 8" stroke="#fff" stroke-width="2.5" fill="none"/></svg>
    </div>
  </section>

  <section class="services-intro">
    <h2 class="section-title">Confira nossos serviços</h2>
    <div class="section-rule"></div>
    <p class="section-text">Da identificação de oportunidades ao suporte contínuo, cuidamos de cada etapa da sua jornada de automação.</p>
  </section>
</body>
</html>
```